Professional business cards for real estate development company

I need business cards for my new real estate development company. The company, "KORVA" is a real estate development, investment, and advisory firm with a focus on multifamily, office, and mixed-use projects across primary and secondary markets in the Southeast United States.

Style preference is modern

Industry/Entity Type

Real Estate Development

Contact Information for Business Card

The business cards need to include:
Name
Title
Mailing Address
Phone Number
Web Address

Logo is attached. I would like white to be the primary color with incorporation of the company colors: #232D3A and #B5A451

Font styles to use
Other font styles liked:
• Montserrat, Avenir

Requirements
Must have
• Company Logo. No need to include the company name since the name is in the logo.
Should not have
• No line type designs

```html
<!DOCTYPE html>
<html lang="en">
<head>
<meta charset="utf-8">
<title>KORVA Business Cards</title>
<link rel="stylesheet" href="https://fonts.googleapis.com/css2?family=Nunito+Sans:wght@300;400;600;700&display=swap">
<style>
  :root {
    --navy: #232D3A;
    --gold: #B5A451;
    --paper: #E4E4E3;
    --stage: #B5A654;
    --ink-soft: #4A4F57;
  }
  * { margin: 0; padding: 0; box-sizing: border-box; }
  html, body { width: 1200px; height: 900px; overflow: hidden; }
  body {
    background: var(--stage);
    font-family: "Nunito Sans", "Avenir", sans-serif;
    position: relative;
  }
  .card {
    position: absolute;
    left: 363px;
    width: 475px;
    height: 271px;
  }
  .card--front {
    top: 145px;
    background: var(--navy);
    display: flex;
    align-items: center;
    justify-content: center;
  }
  .card--back {
    top: 484px;
    background: var(--paper);
  }
  .wordmark {
    font-weight: 700;
    letter-spacing: 6px;
    line-height: 1;
  }
  .card--front .wordmark {
    color: #FFFFFF;
    font-size: 44px;
    margin-top: -10px;
  }
  .card--back .wordmark {
    position: absolute;
    top: 42px;
    left: 0;
    right: 0;
    text-align: center;
    color: var(--navy);
    font-size: 38px;
  }
  .holder {
    position: absolute;
    top: 150px;
    left: 0;
    right: 0;
    text-align: center;
  }
  .holder__name {
    color: var(--navy);
    font-size: 14.5px;
    font-weight: 400;
    line-height: 18px;
  }
  .holder__title {
    color: var(--ink-soft);
    font-size: 11px;
    font-weight: 400;
    line-height: 15px;
  }
  .divider {
    position: absolute;
    top: 192px;
    left: 25px;
    right: 25px;
    height: 1px;
    background: var(--gold);
  }
  .contact {
    position: absolute;
    top: 203px;
    left: 25px;
    font-size: 11px;
    color: var(--ink-soft);
    line-height: 15px;
  }
  .contact__row { display: flex; align-items: center; gap: 6px; }
  .contact__icon { width: 12px; height: 12px; flex: none; }
  .address {
    position: absolute;
    top: 203px;
    right: 25px;
    text-align: right;
    font-size: 11px;
    color: var(--ink-soft);
    line-height: 15px;
  }
</style>
</head>
<body>
  <section class="card card--front">
    <div class="wordmark">KORVA</div>
  </section>

  <section class="card card--back">
    <div class="wordmark">KORVA</div>

    <div class="holder">
      <p class="holder__name">Daniel Vesper</p>
      <p class="holder__title">Managing Partner</p>
    </div>

    <div class="divider"></div>

    <div class="contact">
      <div class="contact__row">
        <svg class="contact__icon" viewBox="0 0 12 12" aria-hidden="true">
          <circle cx="6" cy="6" r="6" fill="var(--gold)"/>
          <path d="M3.6 3.2c.3-.3.7-.3.9 0l.7.9c.2.3.1.6-.1.8l-.4.3c.4.9 1 1.5 1.9 1.9l.3-.4c.2-.2.5-.3.8-.1l.9.7c.3.2.3.6 0 .9l-.5.5c-.4.4-1 .4-1.6.1C5 8.1 3.9 7 3.3 5.7c-.3-.6-.3-1.2.1-1.6z" fill="#FFFFFF"/>
        </svg>
        <span>555-014-2276</span>
      </div>
      <div class="contact__row">
        <svg class="contact__icon" viewBox="0 0 12 12" aria-hidden="true">
          <circle cx="6" cy="6" r="6" fill="var(--gold)"/>
          <rect x="3" y="4" width="6" height="4.2" fill="none" stroke="#FFFFFF" stroke-width="0.8"/>
          <path d="M3 4l3 2.3L9 4" fill="none" stroke="#FFFFFF" stroke-width="0.8"/>
        </svg>
        <span>dvesper@korva.com</span>
      </div>
      <div class="contact__row">
        <svg class="contact__icon" viewBox="0 0 12 12" aria-hidden="true">
          <circle cx="6" cy="6" r="6" fill="var(--gold)"/>
          <circle cx="6" cy="6" r="3" fill="none" stroke="#FFFFFF" stroke-width="0.8"/>
          <ellipse cx="6" cy="6" rx="1.3" ry="3" fill="none" stroke="#FFFFFF" stroke-width="0.7"/>
          <path d="M3 6h6" stroke="#FFFFFF" stroke-width="0.7"/>
        </svg>
        <span>www.korva.com</span>
      </div>
    </div>

    <div class="address">
      <p>2180 Harbor Avenue, Suite 410,</p>
      <p>Savannah, GA 31401</p>
    </div>
  </section>
</body>
</html>
```